Basic / Quick Business Card

Quick easy design project!

Need a one sided basic business card that matches font & style of brand and bottle label for our gourmet condiment, Velvet Corwin Sauce. Velvet Corwin Sauce is sold in specialty retail, gourmet groceries and appears on chef-driven restaurant menus, so the target market is a high end, gourmet, artisan-made food-loving customer.

Files Included:
Sauce Bottle Label
Velvet Corwin Sauce Round Logos

**About the logos - the logo may be used in a circle or alone vertically as on side of the bottle label**

Layout of Card:
May be vertical or horizontal based on designer ideas.

Logo usage (in circle vs. stand alone vertical logo) is up to designers descretion as well.

Reverse side of business card will be various high end / professional product photos / food shots using us.zelk.com system. **Designer on this project will NOT design a reserve for the card.**

Paper that will be used for printing:
Zelk Classic - it's a WHITE paper, but we use a cream background on Velvet Corwin Sauce branding, so please take this into account on design to stay brand consistent.

Elements & Copy for Card:
1. Logo in either script horizontal or vertical version
2. Copy: "Artisan Made - Small Batch"
3. Name - Rory Whitlock
4. Title - Creator
5. Phone - xxx.xxx.xxxx
6. xxxx@velvetcorwin.com
7. URL: velvetcorwinsauce.com
8. Social Media: @getvelvetcorwin on Twitter / Facebook / Instagram

Please provide final files in Illustrator or InDesign format.

```html
<!DOCTYPE html>
<html lang="en">
<head>
<meta charset="utf-8">
<title>Velvet Corwin Sauce – Business Card</title>
<link rel="stylesheet" href="https://fonts.googleapis.com/css2?family=Courier+Prime:wght@400;700&family=Yellowtail&family=Tinos&display=swap">
<style>
  :root {
    --page: #e9e6e6;
    --card-black: #151414;
    --gold: #eba10f;
    --cream: #f1efdb;
    --ink: #1c1a19;
  }
  html, body {
    margin: 0;
    width: 931px;
    height: 1200px;
    overflow: hidden;
    background: var(--page);
  }
  .card {
    position: absolute;
    left: 173px;
    top: 90px;
    width: 585px;
    height: 1021px;
    background: var(--card-black);
  }
  .card__gold-frame {
    position: absolute;
    inset: 22px;
    border: 5px solid var(--gold);
  }
  .card__face {
    position: absolute;
    inset: 31px;
    background: var(--cream);
    border: 3px solid var(--card-black);
    box-shadow: 0 0 0 2px var(--gold);
  }
  .brand {
    position: absolute;
    left: 117px;
    top: 110px;
    width: 346px;
    height: 346px;
    border: 12px solid var(--ink);
    border-radius: 50%;
    box-sizing: border-box;
    display: flex;
    align-items: center;
    justify-content: center;
    text-align: center;
  }
  .brand__name {
    font-family: "Courier Prime", monospace;
    font-weight: 700;
    font-size: 40px;
    line-height: 1.1;
    color: var(--ink);
  }
  .centered {
    position: absolute;
    left: 0;
    right: 0;
    text-align: center;
  }
  .person__name {
    top: 542px;
    font-family: "Yellowtail", cursive;
    font-size: 58px;
    color: var(--gold);
    line-height: 1;
  }
  .person__title {
    top: 628px;
    font-family: "Courier Prime", monospace;
    font-weight: 700;
    font-size: 31px;
    letter-spacing: 6px;
    color: var(--gold);
  }
  .contact {
    top: 730px;
    font-family: "Courier Prime", monospace;
    font-weight: 700;
    font-size: 22px;
    line-height: 35px;
    color: var(--ink);
  }
  .social {
    position: absolute;
    top: 865px;
    left: 0;
    right: 0;
    display: flex;
    align-items: center;
    justify-content: center;
    gap: 20px;
  }
  .social__mark {
    width: 26px;
    height: 26px;
    border-radius: 5px;
    background: var(--gold);
  }
  .social__divider {
    width: 3px;
    height: 42px;
    background: var(--gold);
    margin: 0 4px;
  }
  .social__handle {
    font-family: "Courier Prime", monospace;
    font-weight: 700;
    font-size: 22px;
    color: var(--ink);
  }
  .tagline {
    top: 940px;
    font-family: "Tinos", serif;
    font-size: 22px;
    color: var(--gold);
  }
</style>
</head>
<body>
  <div class="card">
    <div class="card__gold-frame"></div>
    <div class="card__face"></div>

    <div class="brand">
      <span class="brand__name">Velvet<br>Corwin<br>Sauce</span>
    </div>

    <div class="centered person__name">Rory Whitlock</div>
    <div class="centered person__title">CREATOR</div>

    <div class="centered contact">
      123.456.7890<br>
      whitlock@velvetcorwin.com<br>
      www.velvetcorwinsauce.com
    </div>

    <div class="social">
      <span class="social__mark"></span>
      <span class="social__mark"></span>
      <span class="social__mark"></span>
      <span class="social__divider"></span>
      <span class="social__handle">@getvelvetcorwin</span>
    </div>

    <div class="centered tagline">ARTISAN MADE - SMALL BATCH</div>
  </div>
</body>
</html>
```